Business Card for a Mortgage Agent (myself)

I need a business card for my new job as Mortgage Agent. The Broker's logo is to be on the card as well as the brokerage License number. Not sure if to include a photo or not. Info to be on card.
Dante Roux
Mortgage Agent
Lic # M47105386
Cell: 905-614-2753
Email: danterouxk.ma@fennmail.com
Web: www.karlvostermortgages.com
TPW Brokerage Lic. # 73918

```html
<!DOCTYPE html>
<html lang="en">
<head>
<meta charset="utf-8">
<title>Dante Roux – Mortgage Agent Business Cards</title>
<link rel="stylesheet" href="https://fonts.googleapis.com/css2?family=Inter:wght@300;400;800&family=Open+Sans:ital,wght@0,600;1,400&display=swap">
<style>
  :root {
    --brand-blue: #0e4f9f;
    --brand-yellow: #f8c61b;
    --card-white: #f3f2f2;
    --page-bg: #ffffff;
    --muted-grey: #b4b4b4;
    --muted-blue: #4d88d2;
    --ink-blue: #163a6e;
  }
  * { box-sizing: border-box; margin: 0; padding: 0; }
  html, body { width: 1200px; height: 1200px; overflow: hidden; background: var(--page-bg); }
  body { position: relative; font-family: "Inter", sans-serif; }

  .card { position: absolute; overflow: hidden; box-shadow: 0 3px 10px rgba(0,0,0,0.12); }
  .card--light { background: var(--card-white); color: var(--ink-blue); }
  .card--dark { background: var(--brand-blue); color: #ffffff; }

  .card--landscape-light { left: 44px; top: 50px; width: 638px; height: 390px; }
  .card--portrait-dark { left: 765px; top: 50px; width: 391px; height: 638px; }
  .card--portrait-light { left: 53px; top: 506px; width: 391px; height: 640px; }
  .card--landscape-dark { left: 517px; top: 754px; width: 639px; height: 391px; }

  .pos { position: absolute; left: var(--x); top: var(--y); white-space: nowrap; }

  /* Brand lockup */
  .brand { position: absolute; left: var(--x); top: var(--y); width: var(--w);
           display: flex; align-items: center; justify-content: center; gap: 16px; }
  .brand-square { width: 34px; height: 34px; background: var(--brand-yellow); flex: none; }
  .brand-name { font-family: "Inter", sans-serif; font-weight: 800; font-size: 52px;
                letter-spacing: 0.22em; line-height: 1; }
  .card--light .brand-name, .brand--standalone .brand-name { color: var(--brand-blue); }
  .card--dark .brand-name { color: #ffffff; }

  .brand--standalone { position: absolute; left: 496px; top: 560px; width: 208px; }
  .brand--standalone .brand-name { font-size: 58px; }

  /* Bands */
  .band { position: absolute; left: var(--x); top: var(--y); width: var(--w); height: 20px;
          clip-path: polygon(3.5% 0, 100% 0, 96.5% 100%, 0 100%);
          display: flex; align-items: center; justify-content: center; }
  .band--edge { clip-path: polygon(4% 0, 100% 0, 100% 100%, 0 100%); }
  .card--light .band { background: var(--brand-blue); color: #ffffff; }
  .card--dark .band { background: #ffffff; color: var(--brand-blue); }
  .band-title { font-family: "Open Sans", sans-serif; font-weight: 600; font-size: 12px; letter-spacing: 0.14em; }
  .band--tall { height: 24px; }
  .band--tall .band-title { font-size: 14px; }
  .band-url { font-family: "Open Sans", sans-serif; font-style: italic; font-size: 16px; }

  /* Agent details */
  .agent-name { font-weight: 800; font-size: 33px; line-height: 1; letter-spacing: -0.01em; }
  .card--light .agent-name { color: var(--brand-blue); }
  .card--dark .agent-name { color: var(--brand-yellow); }
  .agent-title { font-weight: 400; font-size: 22px; line-height: 1; }
  .title-rule { height: 2px; width: 196px; background: var(--brand-yellow); }
  .licence { font-size: 13px; font-weight: 400; line-height: 1; }
  .card--light .licence { color: var(--muted-grey); }
  .card--dark .licence { color: var(--muted-blue); }
  .licence--right { left: auto; right: var(--r); }

  .contact { font-weight: 300; font-size: 21px; line-height: 27px; }
  .contact--compact { font-size: 19px; line-height: 26px; }
  .website { font-weight: 300; font-size: 20px; line-height: 1; }
</style>
</head>
<body>

  <!-- Landscape, light -->
  <section class="card card--light card--landscape-light">
    <div class="brand" style="--x:96px;--y:76px;--w:176px"><span class="brand-square"></span><span class="brand-name">TPW</span></div>
    <div class="band" style="--x:52px;--y:180px;--w:264px"><span class="band-title">TRUE PATH WEALTH</span></div>
    <div class="band band--edge" style="--x:320px;--y:180px;--w:318px"><span class="band-url">www.karlvostermortgages.com</span></div>
    <p class="pos licence licence--right" style="--r:41px;--y:211px">TPW Brokerage Lic. # 73918</p>
    <h2 class="pos agent-name" style="--x:98px;--y:248px">Dante Roux</h2>
    <p class="pos agent-title" style="--x:98px;--y:283px">Mortgage Agent</p>
    <div class="pos title-rule" style="--x:98px;--y:311px"></div>
    <p class="pos licence" style="--x:98px;--y:321px">Lic # M47105386</p>
    <p class="pos contact contact--compact" style="--x:334px;--y:312px">phone: (905) 614-2753<br>danterouxk.ma@fennmail.com</p>
  </section>

  <!-- Portrait, dark -->
  <section class="card card--dark card--portrait-dark">
    <div class="brand" style="--x:107px;--y:92px;--w:176px"><span class="brand-square"></span><span class="brand-name">TPW</span></div>
    <div class="band" style="--x:63px;--y:194px;--w:264px"><span class="band-title">TRUE PATH WEALTH</span></div>
    <h2 class="pos agent-name" style="--x:52px;--y:294px">Dante Roux</h2>
    <p class="pos agent-title" style="--x:52px;--y:330px">Mortgage Agent</p>
    <div class="pos title-rule" style="--x:52px;--y:357px"></div>
    <p class="pos licence" style="--x:52px;--y:366px">Lic # M47105386</p>
    <p class="pos contact" style="--x:52px;--y:389px">phone: (905) 614-2753<br>danterouxk.ma@fennmail.com</p>
    <p class="pos website" style="--x:52px;--y:528px">www.karlvostermortgages.com</p>
    <p class="pos licence" style="--x:52px;--y:562px">TPW Brokerage Lic. # 73918</p>
  </section>

  <!-- Portrait, light -->
  <section class="card card--light card--portrait-light">
    <div class="brand" style="--x:91px;--y:100px;--w:208px"><span class="brand-square"></span><span class="brand-name">TPW</span></div>
    <div class="band band--tall" style="--x:39px;--y:220px;--w:312px"><span class="band-title">TRUE PATH WEALTH</span></div>
    <h2 class="pos agent-name" style="--x:52px;--y:296px">Dante Roux</h2>
    <p class="pos agent-title" style="--x:52px;--y:330px">Mortgage Agent</p>
    <div class="pos title-rule" style="--x:52px;--y:357px"></div>
    <p class="pos licence" style="--x:52px;--y:366px">Lic # M47105386</p>
    <p class="pos contact" style="--x:52px;--y:389px">phone: (905) 614-2753<br>danterouxk.ma@fennmail.com</p>
    <p class="pos website" style="--x:52px;--y:532px">www.karlvostermortgages.com</p>
    <p class="pos licence" style="--x:52px;--y:564px">TPW Brokerage Lic. # 73918</p>
  </section>

  <!-- Standalone brand lockup -->
  <div class="brand brand--standalone"><span class="brand-square"></span><span class="brand-name">TPW</span></div>

  <!-- Landscape, dark -->
  <section class="card card--dark card--landscape-dark">
    <div class="brand" style="--x:95px;--y:78px;--w:180px"><span class="brand-square"></span><span class="brand-name">TPW</span></div>
    <div class="band" style="--x:51px;--y:180px;--w:264px"><span class="band-title">TRUE PATH WEALTH</span></div>
    <div class="band band--edge" style="--x:319px;--y:180px;--w:320px"><span class="band-url">www.karlvostermortgages.com</span></div>
    <p class="pos licence licence--right" style="--r:51px;--y:210px">TPW Brokerage Lic. # 73918</p>
    <h2 class="pos agent-name" style="--x:98px;--y:245px">Dante Roux</h2>
    <p class="pos agent-title" style="--x:98px;--y:281px">Mortgage Agent</p>
    <div class="pos title-rule" style="--x:98px;--y:309px"></div>
    <p class="pos licence" style="--x:98px;--y:318px">Lic # M47105386</p>
    <p class="pos contact contact--compact" style="--x:335px;--y:314px">phone: (905) 614-2753<br>danterouxk.ma@fennmail.com</p>
  </section>

</body>
</html>
```